Lantern Hour book needs a cover design

I need a front and back cover design that demonstrates a strong sense of possibility that trust can be repaired even if things look bleak. Repairing trust is difficult, but this book is full of wisdom, proven strategies, and doctoral research to help people strengthen relationships and improve trust. It can help any group: business, nonprofit, education, service. Showing diversity of groups and people is very important. For the cover title, there should be a play on words: "Lantern Hour: Is it? Possible" should have the words "is it?" crossed out and the words "It IS! should be replaced there in a striking way. Perhaps in red ink. For publishing purposes, book will be titled Lantern Hour: It IS Possible! Please see the attachment for an example. The book layout is approximately 260 pages.

Target Market(s)

A business self-help book, but the target is any person in a group that feels they have lost trust in each other. It can be just a normal person struggling in a volunteer group they are a part of, or a supervisor whose group is not working well together. It can be a leader who just wants their group to be stronger.

Industry/Entity Type

Business Management

Font styles to use
Other font styles liked:
• Allise - I believe is being used on the interior of the book for the title page and headings

Requirements
Must have
• Show hope and possibility in the midst of difficulty. Must have a play on the words in the title "Lantern Hour: Is it? Possible" with crossing out "is it?" with "It IS!" (see attached example) Must include the author's name: Marla Quinby, PhD Must include a smaller tagline: "Proven Strategies to Help Groups Get Unstuck"
Nice to have
• Showing diverse people, or hands. Diverse kinds of groups - not just business. A colorful cover. Maybe show the complexity of trust when it is broken...broken pieces of trust that are then picked up and put together when people work together. Could show people (or images of hands) or other ways to show that it's a choice and it is possible to repair broken trust. I'd also like to convey a sense of a group - not just random people. That they have something at stake to work on repairing trust together and this book can help them.
Should not have
• If images of people are used, just showing one gender or race is not okay. Nor just binary choices: like an image containing one man and one woman, or one white person and one person of color - otherwise it seems that the book on Lantern Hour is about race or gender relations.

```html
<!DOCTYPE html>
<html lang="en">
<head>
<meta charset="utf-8">
<title>Lantern Hour: It IS Possible! — Front Cover</title>
<link rel="stylesheet" href="https://fonts.googleapis.com/css2?family=Tenor+Sans&display=swap">
<style>
  :root {
    --page-bg: #f3f3f3;
    --cover-top: #f7f8fb;
    --cover-bottom: #e9edf4;
    --navy: #1e2456;
    --ink-red: #e0141e;
    --art-green: #b9c98e;
    --art-mauve: #c9b3bd;
    --art-grey: #cfd5de;
  }
  * { box-sizing: border-box; margin: 0; padding: 0; }
  html, body {
    width: 1200px;
    height: 1200px;
    overflow: hidden;
    background: var(--page-bg);
  }
  .canvas {
    position: relative;
    width: 1200px;
    height: 1200px;
    display: flex;
    align-items: center;
    justify-content: center;
  }
  .cover {
    position: relative;
    width: 800px;
    height: 1110px;
    background: linear-gradient(180deg, var(--cover-top) 0%, var(--cover-bottom) 100%);
    box-shadow: 0 6px 24px rgba(20, 24, 60, 0.12);
    font-family: "Tenor Sans", "Optima", sans-serif;
    color: var(--navy);
    text-align: center;
  }
  .title {
    position: absolute;
    top: 38px;
    left: 0;
    right: 0;
    font-weight: 400;
    line-height: 0.98;
    letter-spacing: 2px;
  }
  .title .line {
    display: block;
    font-size: 148px;
  }
  .wordplay {
    position: absolute;
    top: 378px;
    left: 0;
    right: 0;
    height: 120px;
  }
  .wordplay .replacement {
    position: absolute;
    left: 352px;
    top: 0;
    font-size: 52px;
    transform: rotate(-14deg);
    transform-origin: left bottom;
    letter-spacing: 2px;
  }
  .wordplay .question {
    position: absolute;
    left: 330px;
    top: 62px;
    font-size: 54px;
    letter-spacing: 1px;
    white-space: nowrap;
  }
  .struck {
    position: relative;
    display: inline-block;
  }
  .struck svg {
    position: absolute;
    left: -6px;
    top: 8px;
    width: calc(100% + 10px);
    height: 48px;
    overflow: visible;
  }
  .possible {
    position: absolute;
    top: 510px;
    left: 0;
    right: 0;
    font-size: 128px;
    letter-spacing: 3px;
    line-height: 1;
    z-index: 2;
  }
  .handshake-art {
    position: absolute;
    left: 70px;
    top: 600px;
    width: 660px;
    height: 380px;
    border-radius: 50%;
    background:
      radial-gradient(ellipse at 50% 55%, rgba(185, 201, 142, 0.75) 0%, rgba(201, 179, 189, 0.35) 45%, rgba(207, 213, 222, 0) 72%);
  }
  .tagline {
    position: absolute;
    top: 988px;
    left: 0;
    right: 0;
    font-size: 25px;
    letter-spacing: 1.5px;
    line-height: 1.3;
    text-transform: uppercase;
  }
  .author {
    position: absolute;
    top: 1060px;
    left: 0;
    right: 0;
    font-size: 32px;
    letter-spacing: 2px;
  }
</style>
</head>
<body>
  <main class="canvas">
    <section class="cover">
      <h1 class="title">
        <span class="line">LANTERN</span>
        <span class="line">HOUR</span>
      </h1>

      <div class="wordplay">
        <span class="replacement">IT IS</span>
        <span class="question">IS<span class="struck">IT<svg viewBox="0 0 60 48" preserveAspectRatio="none" aria-hidden="true">
              <line x1="2" y1="4" x2="58" y2="44" stroke="var(--ink-red)" stroke-width="4" stroke-linecap="round"/>
              <line x1="58" y1="4" x2="2" y2="44" stroke="var(--ink-red)" stroke-width="4" stroke-linecap="round"/>
            </svg></span>?</span>
      </div>

      <div class="possible">POSSIBLE</div>

      <div class="handshake-art" role="img" aria-label="Low-poly wireframe illustration of two hands joined in a handshake, in soft green and mauve tones"></div>

      <p class="tagline">Proven strategies to help<br>groups get unstuck</p>

      <p class="author">MARLA QUINBY, Ph.D.</p>
    </section>
  </main>
</body>
</html>
```